Website Redesign Brief for Breezeline Cooling Services WA

Creating a clear and concise brief for designers to redesign your website, https://breezelinecowa.com.au/, is essential to ensure the project aligns with your vision for a more energetic, friendly, optimistic, and user-friendly website. Below is a sample brief tailored to your request, balancing specificity with flexibility to allow designers to bring their creativity to the table.

Website Redesign Brief for Breezeline Co WA
1. Project Overview

We are seeking a redesign of our website, https://breezelinecowa.com.au/, to create a vibrant, engaging, and user-friendly online presence that reflects our brand’s commitment to providing top-notch air conditioning services in Western Australia. The redesigned website should feel energetic, friendly, and optimistic while maintaining professionalism and improving user experience.
2. Goals and Objectives

Enhance Brand Perception: Convey a modern, approachable, and positive brand identity that resonates with both residential and commercial clients.
Improve User Experience: Simplify navigation, improve accessibility, and ensure a seamless experience across devices (desktop, tablet, mobile).
Increase Engagement: Encourage visitors to explore services, request quotes, and contact us through clear calls-to-action (CTAs).
Boost Conversion Rates: Make it easier for users to find information and take action (e.g., booking services or inquiries).
Showcase Expertise: Highlight our professional air conditioning services, experience, and customer satisfaction in an inviting way.

3. Target Audience

Primary Audience: Homeowners and small business owners in Western Australia seeking air conditioning installation, maintenance, or repair services.
Secondary Audience: Property managers, commercial clients, and real estate professionals looking for reliable HVAC solutions.
Demographics: Ages 25–65, mix of tech-savvy and non-tech-savvy users, located primarily in Perth and surrounding areas.
User Needs: Clear information about services, transparent pricing, easy contact options, and reassurance of quality and reliability.

4. Design Preferences

Tone and Style:

Energetic: Use bold, vibrant colors (e.g., blues, whites, and pops of warm tones like orange or yellow) to evoke energy and optimism.
Friendly: Incorporate approachable language, welcoming imagery, and a clean, uncluttered layout.
Optimistic: Highlight positive customer outcomes (e.g., comfort, energy savings) through visuals and messaging.
Professional yet approachable: Maintain credibility as a trusted service provider while avoiding a cold or overly corporate feel.

Visual Elements:

Use high-quality images of happy customers, comfortable homes/offices, and modern air conditioning units.
Incorporate subtle animations or micro-interactions to add energy (e.g., hover effects on buttons or smooth scrolling).
Avoid overly complex graphics that may slow down the site or distract from usability.

Typography: Clean, modern fonts that are easy to read. Use larger, bold headings for hierarchy and warmth.
Inspiration: Websites like https://www.frostvale.com.au/ (clean and professional) or https://www.quellarpowertech.com.au/ (user-friendly and modern) but with a more vibrant and welcoming vibe.

5. Functional Requirements

User-Friendly Navigation: Simplify the menu structure to make key pages (e.g., Services, About Us, Contact) easily accessible.
Mobile Responsiveness: Ensure the site is fully optimized for mobile devices, with fast load times and intuitive touch interactions.
Key Features:

Prominent CTAs for requesting quotes, booking services, or contacting the team.
A clear service overview with icons or visuals for each service (e.g., installation, repairs, maintenance).
A testimonials section to showcase customer satisfaction.
An easy-to-use contact form with minimal fields.
Integration with Google Maps for location-based services or office directions.

SEO and Performance: Optimize for search engines (e.g., keywords like “air conditioning Perth”) and ensure fast loading speeds.
Accessibility: Follow WCAG guidelines to ensure the site is usable for all visitors, including those with disabilities.

6. Content Guidance

Existing Content: Review and refine current content from https://breezelinecowa.com.au/ to make it concise, engaging, and aligned with the friendly tone.
New Content Ideas:

Add a “Why Choose Us” section highlighting expertise, customer service, and eco-friendly solutions.
Include a FAQ page to address common customer questions.
Create a blog section for tips on air conditioning maintenance or energy efficiency (optional).

Tone of Voice: Conversational, reassuring, and positive. Avoid technical jargon unless clearly explained.

7. Technical Considerations

Platform: Open to recommendations (e.g., WordPress, Wix, or custom-built) but prioritize ease of maintenance and scalability.
Integrations: Ensure compatibility with existing tools (e.g., Google Analytics, CRM for quote requests, or booking systems).
Domain and Hosting: Retain current domain (breezelinecowa.com.au); hosting recommendations welcome.
Timeline: Initial design concepts within [insert timeline, e.g., 2–3 weeks], with full redesign completed by [insert deadline, e.g., 6–8 weeks].
Budget: [Insert budget range or state “flexible, please provide a quote”].

8. Deliverables

Wireframes and mockups for homepage, service pages, and contact page.
Fully responsive website design with all necessary pages.
Style guide (colors, fonts, imagery guidelines).
CMS setup (if applicable) with basic training for content updates.
Testing and optimization for performance and SEO.

9. Success Metrics

Increased time on site and reduced bounce rate.
Higher conversion rates for quote requests and contact form submissions.
Positive user feedback on ease of navigation and overall experience.
Improved search engine rankings for key terms within [insert timeframe, e.g., 3 months].

10. Additional Notes

Please provide a portfolio of similar projects or examples of user-friendly, vibrant websites.
We are open to creative suggestions to make the website stand out in the HVAC industry.
Regular progress updates and collaboration during the design process are appreciated.
Updates

designers are asking for more time

few have requested an extension. I Have extended

Target Market(s)

Primary Audience: Homeowners and small business owners in Western Australia seeking air conditioning installation, maintenance, or repair services. Secondary Audience: Property managers, commercial clients, and real estate professionals looking for reliable HVAC solutions. Demographics: Ages 25–65, mix of tech-savvy and non-tech-savvy users, located primarily in Perth and surrounding areas. User Needs: Clear information about services, transparent pricing, easy contact options, and reassurance of quality and reliability.

Industry/Entity Type

Air Conditioning and Refrigeration (HVAC & R)

Coding

Coded - Design and coding required

Colors
0054AA
0677BA
7BADD7
CADEEF
E8F1F8
59FF00
82FF00
B8FF75
E3FFCB
F4FFEA
F0912C
F2A743
F7CA91
FBE8D2
FDF5EE
EE7325
F08F49
F5BC92
FAE3D3
FDF4ED

Requirements
Must have
• Must have all my current information I currently have on my web page.
Nice to have
• A sales page for people to buy products online

```html
<!DOCTYPE html>
<html lang="en">
<head>
<meta charset="utf-8">
<title>Contact — Tharrowind WA</title>
<link href="https://fonts.googleapis.com/css2?family=Poppins:wght@500;600;700&family=Inter:wght@400;500;600&display=swap" rel="stylesheet">
<style>
:root{
  --orange:#EE7325;
  --orange-soft:#F08F49;
  --peach:#FBE8D2;
  --peach-light:#FDF5EE;
  --sky:#E8F1F8;
  --blue:#0054AA;
  --ink:#141414;
  --body:#4a4a4a;
  --white:#ffffff;
  --dark:#1d1612;
}
*{box-sizing:border-box;margin:0;padding:0}
html,body{width:1200px;height:2744px;overflow:hidden}
body{font-family:"Inter",sans-serif;color:var(--ink);background:var(--white);position:relative}
h1,h2,h3,h4{font-family:"Poppins",sans-serif}

.site-header{position:absolute;top:0;left:0;width:1200px;height:150px;display:flex;align-items:center;justify-content:space-between;padding:0 100px}
.brand{display:flex;align-items:center;gap:12px;font-family:"Poppins",sans-serif;font-weight:600;font-size:20px;color:var(--ink)}
.brand-mark{width:34px;height:34px;border-radius:50%;background:var(--orange)}
.main-nav{display:flex;align-items:center;gap:28px;font-size:15px}
.main-nav a{color:var(--ink);text-decoration:none}
.main-nav a.current{color:var(--orange)}
.btn-outline{border:2px solid var(--ink);border-radius:24px;padding:10px 20px;font-weight:600;font-size:13px;letter-spacing:.3px}

.hero{position:absolute;top:150px;left:0;width:1200px;height:350px;background:linear-gradient(90deg,#1a120e 0%,#2a1c15 45%,#6b5446 70%,#a08979 100%)}
.hero h1{position:absolute;left:210px;top:115px;color:var(--white);font-size:40px;line-height:1.25;font-weight:600}

.offices{position:absolute;top:500px;left:0;width:1200px;height:510px;background:var(--sky);text-align:center}
.section-title{font-size:30px;font-weight:600}
.offices .section-title{margin-top:78px}
.section-sub{font-size:15px;color:var(--body);margin-top:10px}
.office-grid{display:flex;gap:20px;padding:0 100px;margin-top:44px}
.office-card{flex:1;background:var(--peach);padding:30px 24px;text-align:left;height:220px}
.office-card h3{font-size:22px;font-weight:600;margin-bottom:22px}
.info{display:flex;gap:12px;font-size:14px;color:var(--body);margin-bottom:14px;line-height:1.45}
.info svg{flex:none;margin-top:2px}

.faq{position:absolute;top:1010px;left:0;width:1200px;height:630px;background:linear-gradient(180deg,#2b2622 0%,#3e3630 50%,#2a2420 100%);text-align:center;color:var(--white)}
.faq .section-title{margin-top:80px}
.faq .section-sub{color:#e6e6e6}
.faq-grid{display:grid;grid-template-columns:1fr 1fr;gap:35px 20px;padding:0 100px;margin-top:44px;text-align:left}
.faq-card{background:var(--white);color:var(--ink);padding:26px 30px;height:180px}
.faq-card h3{font-size:24px;font-weight:600;line-height:1.3;margin-bottom:12px}
.faq-card p{font-size:14px;color:var(--body);line-height:1.55}

.contact{position:absolute;top:1640px;left:0;width:1200px;height:660px;background:var(--white)}
.form-box{position:absolute;left:100px;top:140px;width:480px;height:420px;background:var(--peach);padding:36px 34px}
.row{display:flex;gap:20px}
.field{flex:1;margin-bottom:22px}
.field label{display:block;font-size:13px;margin-bottom:8px}
.field .input{height:36px;background:var(--peach-light);border:1px solid #e6cdb3}
.field .area{height:100px;background:var(--peach-light);border:1px solid #e6cdb3}
.btn-solid{display:inline-block;background:var(--orange);color:var(--white);font-weight:600;font-size:13px;padding:11px 18px;border-radius:4px}
.contact-info{position:absolute;left:655px;top:120px;width:445px}
.contact-info h2{font-size:30px;font-weight:600}
.contact-info p.lead{font-size:14px;color:var(--body);margin:12px 0 26px}
.contact-info h4{font-size:22px;font-weight:600;margin-bottom:16px}
.socials{display:flex;gap:14px;margin-top:4px}
.socials span{width:14px;height:14px;border-radius:50%;background:var(--ink)}

.cta{position:absolute;top:2300px;left:0;width:1200px;height:290px;background:linear-gradient(90deg,#1c1613,#2d231e,#1c1613);text-align:center;color:var(--white)}
.cta h2{font-size:32px;font-weight:600;line-height:1.35;margin-top:72px}
.cta p{font-size:14px;color:#e4e4e4;line-height:1.6;width:640px;margin:14px auto 24px}
.cta .btn-solid{border-radius:24px;padding:12px 26px}

.site-footer{position:absolute;top:2590px;left:0;width:1200px;height:154px;display:flex;justify-content:space-between;align-items:center;padding:0 100px;font-size:14px}
.footer-nav{display:flex;gap:22px}
.footer-nav a{color:var(--ink);text-decoration:none}
.footer-nav a.current{color:var(--orange)}
</style>
</head>
<body>

<header class="site-header">
  <div class="brand"><span class="brand-mark"></span>Tharrowind WA</div>
  <nav class="main-nav">
    <a href="#">Home</a><a href="#">About</a><a href="#">Services</a><a href="#">Blog</a><a class="current" href="#">Contact</a>
    <span class="btn-outline">REQUEST A QUOTE</span>
  </nav>
</header>

<section class="hero" role="img" aria-label="Photo of a smiling woman adjusting a wall air conditioner at home">
  <h1>Get In Touch With<br>Tharrowind WA</h1>
</section>

<section class="offices">
  <h2 class="section-title">We’re Here To Assist You Anytime!</h2>
  <p class="section-sub">Reach out to our friendly team for all air conditioning needs and inquiries.</p>
  <div class="office-grid">
    <div class="office-card">
      <h3>Perth Office</h3>
      <div class="info"><svg width="14" height="14" viewBox="0 0 24 24"><path d="M2 5h20v14H2z" fill="#141414"/><path d="M2 5l10 8 10-8" stroke="#FBE8D2" stroke-width="2" fill="none"/></svg>perth@tharrowindwa.com.au</div>
      <div class="info"><svg width="14" height="14" viewBox="0 0 24 24"><path d="M6 2l4 5-2 3c1 3 3 5 6 6l3-2 5 4-3 4C10 22 2 14 2 5z" fill="#141414"/></svg>08 5550 1824</div>
      <div class="info"><svg width="14" height="14" viewBox="0 0 24 24"><path d="M12 2a7 7 0 017 7c0 5-7 13-7 13S5 14 5 9a7 7 0 017-7z" fill="#141414"/><circle cx="12" cy="9" r="2.5" fill="#FBE8D2"/></svg>14 Coolwater Rd, Perth WA 6000, Australia</div>
    </div>
    <div class="office-card">
      <h3>Fremantle Office</h3>
      <div class="info"><svg width="14" height="14" viewBox="0 0 24 24"><path d="M2 5h20v14H2z" fill="#141414"/><path d="M2 5l10 8 10-8" stroke="#FBE8D2" stroke-width="2" fill="none"/></svg>fremantle@tharrowindwa.com.au</div>
      <div class="info"><svg width="14" height="14" viewBox="0 0 24 24"><path d="M6 2l4 5-2 3c1 3 3 5 6 6l3-2 5 4-3 4C10 22 2 14 2 5z" fill="#141414"/></svg>08 5550 2731</div>
      <div class="info"><svg width="14" height="14" viewBox="0 0 24 24"><path d="M12 2a7 7 0 017 7c0 5-7 13-7 13S5 14 5 9a7 7 0 017-7z" fill="#141414"/><circle cx="12" cy="9" r="2.5" fill="#FBE8D2"/></svg>27 Harbourbreeze Ave, Fremantle WA 6160, Australia</div>
    </div>
    <div class="office-card">
      <h3>Bunbury Office</h3>
      <div class="info"><svg width="14" height="14" viewBox="0 0 24 24"><path d="M2 5h20v14H2z" fill="#141414"/><path d="M2 5l10 8 10-8" stroke="#FBE8D2" stroke-width="2" fill="none"/></svg>bunbury@tharrowindwa.com.au</div>
      <div class="info"><svg width="14" height="14" viewBox="0 0 24 24"><path d="M6 2l4 5-2 3c1 3 3 5 6 6l3-2 5 4-3 4C10 22 2 14 2 5z" fill="#141414"/></svg>08 5550 3648</div>
      <div class="info"><svg width="14" height="14" viewBox="0 0 24 24"><path d="M12 2a7 7 0 017 7c0 5-7 13-7 13S5 14 5 9a7 7 0 017-7z" fill="#141414"/><circle cx="12" cy="9" r="2.5" fill="#FBE8D2"/></svg>9 Southwind Pde, Bunbury WA 6230, Australia</div>
    </div>
  </div>
</section>

<section class="faq" role="img" aria-label="Background photo of a team meeting in an office, darkened">
  <h2 class="section-title">Frequently Asked Questions</h2>
  <p class="section-sub">Find answers to common questions about our air conditioning services.</p>
  <div class="faq-grid">
    <div class="faq-card"><h3>What Air Conditioning Services Do You Provide?</h3><p>We specialise in installation, repairs, and maintenance of split systems, ducted air conditioning, and energy-efficient solutions.</p></div>
    <div class="faq-card"><h3>Do You Offer Emergency Services?</h3><p>Yes, we provide 24/7 emergency callouts to ensure your comfort is never compromised.</p></div>
    <div class="faq-card"><h3>Are Your Technicians Licensed?</h3><p>Absolutely! All our technicians are fully licensed and trained to ensure high-quality service delivery.</p></div>
    <div class="faq-card"><h3>What Warranty Do You Offer?</h3><p>We provide a workmanship warranty on all installations and repairs for your peace of mind.</p></div>
  </div>
</section>

<section class="contact">
  <div class="form-box">
    <div class="row">
      <div class="field"><label>First name</label><div class="input"></div></div>
      <div class="field"><label>Last name</label><div class="input"></div></div>
    </div>
    <div class="field"><label>Email address</label><div class="input"></div></div>
    <div class="field"><label>Type your message...</label><div class="area"></div></div>
    <span class="btn-solid">SUBMIT</span>
  </div>
  <div class="contact-info">
    <h2>Contact Us Today!</h2>
    <p class="lead">Fill out the form, and our team will get back to you promptly.</p>
    <h4>Stay Connected</h4>
    <div class="info"><svg width="14" height="14" viewBox="0 0 24 24"><path d="M2 5h20v14H2z" fill="#141414"/><path d="M2 5l10 8 10-8" stroke="#fff" stroke-width="2" fill="none"/></svg>info@tharrowindwa.com.au</div>
    <div class="info"><svg width="14" height="14" viewBox="0 0 24 24"><path d="M6 2l4 5-2 3c1 3 3 5 6 6l3-2 5 4-3 4C10 22 2 14 2 5z" fill="#141414"/></svg>+61 400 555 019</div>
    <div class="info"><svg width="14" height="14" viewBox="0 0 24 24"><path d="M12 2a7 7 0 017 7c0 5-7 13-7 13S5 14 5 9a7 7 0 017-7z" fill="#141414"/><circle cx="12" cy="9" r="2.5" fill="#fff"/></svg>38 Chillside Street, Perth WA 6000, Australia</div>
    <h4 style="margin-top:20px">Let’s Socialize</h4>
    <div class="socials"><span></span><span></span><span></span></div>
  </div>
</section>

<section class="cta" role="img" aria-label="Dark background photo of a modern living room with air conditioning">
  <h2>Contact Us For Quality Air Solutions<br>Now!</h2>
  <p>Tharrowind WA is your go-to partner for all air conditioning needs. We provide quality services that ensure comfort and satisfaction for every client.</p>
  <span class="btn-solid">REQUEST A QUOTE</span>
</section>

<footer class="site-footer">
  <nav class="footer-nav"><a href="#">Home</a><a href="#">About</a><a href="#">Services</a><a href="#">Blog</a><a class="current" href="#">Contact</a></nav>
  <p>Copyright © 2025 Tharrowind WA</p>
</footer>

</body>
</html>
```